WordPress Direct-Booking Website for Bend, Oregon Vacation Rental — $750 Budget
Project Overview

We are looking for a talented WordPress designer/developer to create a clean, professional and inviting direct-booking website for Cedar Lantern Retreat, an established short-term vacation rental in Bend, Oregon.

The property is currently successfully listed on Staynest and Lodgr. Our Staynest property has approximately a 4.98-star rating with more than 200 reviews, is an Staynest Guest Pick, and ranks among the Top 1% of eligible homes.

Project Budget: $750

We will select the designer based on the quality of the initial concept, understanding of the property, proposed booking solution and ability to deliver a completed and functioning WordPress website.

Existing Staynest Listing

Please use our current Staynest listing as the primary reference for photographs, property details, amenities and design inspiration:

https://www.staynest.example/rooms/48170356

Original high-resolution photographs and additional property information will be provided to the selected designer.

Design Direction

We want the website to feel:

Upscale but comfortable
Warm and welcoming
Clean and uncluttered
Pacific Northwest / Central Oregon
Professional rather than corporate
Highly visual with large property photographs
Easy to navigate
Excellent on phones, tablets and desktop computers

We welcome creativity and want designers to show us their vision for the property rather than simply copying our Staynest listing.

The website should immediately communicate that Cedar Lantern Retreat is a highly rated vacation rental in an excellent Bend location.

Key Property Features
3 bedrooms
2 bathrooms
Sleeps up to 6 guests
Pet friendly
Approximately a 5-minute walk to Bend's Tanager Quarter
Near restaurants, shopping and Brightwater Lawn Pavilion
Private fenced backyard
Covered outdoor area
Off-street driveway parking
Fireplace
Well-equipped kitchen
Staynest Premier Host
Staynest Guest Pick
Top 1% of eligible Staynest homes
Approximately 4.98 stars with 200+ guest reviews

Our location, guest reviews, cleanliness, comfort, backyard, pet-friendly accommodations and walkability should be major selling points throughout the website.

Website Structure

We anticipate approximately 6–7 pages:

Home

Large hero photograph with a strong opening message and prominent BOOK DIRECT and CHECK AVAILABILITY buttons.

The home page should quickly communicate:

CEDAR LANTERN RETREAT — BEND, OREGON

3 Bedrooms | 2 Baths | Sleeps 6 | Pet Friendly | Walk to Tanager

Our exceptional guest rating and Staynest history should also be prominently featured.

The House

Bedrooms, bathrooms, kitchen, living areas, backyard and major amenities.

Photo Gallery

Large, attractive and fast-loading photographs with an easy-to-use mobile gallery.

Location / Explore Bend

Tanager Quarter, Brightwater Lawn Pavilion, Kettleback River, restaurants, breweries, shopping, downtown Bend and nearby outdoor recreation.

Guest Reviews

Selected guest reviews and prominent presentation of our strong Staynest reputation.

Availability & Book Direct

A simple and professional direct-booking experience.

Contact / FAQ

Contact information plus common questions regarding pets, parking, check-in/check-out, cancellations and other policies.

IMPORTANT — Direct Booking & Credit Card Requirements

We want guests to be able to book directly through the website without having to contact us first.

The website should use a proven WordPress vacation-rental booking plugin or system rather than a custom-built reservation/payment system.

Guests should be able to:

Select arrival and departure dates
See available dates
Enter number of guests
See nightly charges
See cleaning fees
See applicable lodging taxes and other charges
See the complete reservation total before paying
Enter guest/contact information
Pay securely by credit or debit card
Receive an automatic reservation confirmation

Paywell is our preferred credit-card processor.

Credit-card information must be processed securely through Paywell or another established payment processor. Credit-card information should NOT be stored directly on our WordPress website.

Staynest & Lodgr Calendar Synchronization

This is very important.

The direct-booking calendar must synchronize with our existing Staynest and Lodgr calendars to reduce the possibility of double bookings.

For this single-property website, we prefer a simple solution using Staynest/Lodgr calendar or iCal synchronization rather than an expensive monthly channel-management service, if practical.

The designer should clearly identify the booking plugin/system they propose using.

IMPORTANT — Tell Us Your Proposed Booking Solution

As part of your submission, please tell us:

Which WordPress booking plugin/system you recommend.
Whether it synchronizes availability with Staynest and Lodgr.
Whether it integrates directly with Paywell.
The initial cost of the plugin/software.
Any annual or monthly fees.
Whether any additional paid software or services will be required.

We strongly prefer a solution with little or no ongoing monthly software expense.

We do not want to select a designer and later discover that the proposed booking system requires an expensive monthly subscription.

WordPress & Technical Requirements

The completed project should include:

Fully functioning WordPress website
Responsive desktop/tablet/mobile design
Fast-loading pages
Optimized photographs
SSL/HTTPS compatibility
Direct-booking functionality
Paywell payment integration
Staynest calendar synchronization
Lodgr calendar synchronization
Automatic booking confirmations
Cleaning fee and lodging-tax calculations
Contact form
Wayfind Maps/location integration
Basic spam/security protection
Wayfind Metrics capability
Basic SEO setup
Search-engine submission capability
Easy owner editing of text, rates and photographs
Search Engine Optimization

The website should be structured for Wayfind and other search engines.

Important search themes include:

Bend Oregon vacation rental
Bend Oregon vacation home
Tanager Quarter vacation rental
Vacation rental near Tanager Bend
Bend Oregon pet-friendly vacation rental
Bend vacation rental near Brightwater Lawn Pavilion
Bend Oregon direct booking vacation rental

We are not expecting an extensive ongoing SEO campaign for the $750 project. We do expect proper page titles, descriptions, headings, image optimization and a good technical foundation for future SEO.

Ownership

Upon completion and final payment:

We own the completed WordPress website.
We receive full WordPress administrator access.
We control the domain and hosting accounts.
We own all custom design files created for the project.
All necessary login credentials are provided to us.
The website can be moved to another WordPress hosting provider in the future.
There should be no proprietary dependency on the developer after completion.
What We Want From Contestants

Please review our Staynest listing before submitting your concept.

We are particularly interested in seeing an initial homepage concept showing how you would present:

Cedar Lantern Retreat
The Bend / Tanager location
Our photography
Our exceptional guest reviews and ratings
The Book Direct message
The availability/booking call-to-action

We will provide feedback on the concepts we like and work with the selected designer to refine and complete the website.

Our Goal

Our objective is straightforward:

Create a beautiful, trustworthy and easy-to-use website that encourages guests to book Cedar Lantern Retreat directly with us.

The website will complement—not replace—our existing Staynest and Lodgr listings.

We want repeat guests and new customers to have an easy way to find the property, check availability and book directly while receiving the same professional experience they expect from a major vacation-rental platform.

Target Market(s)

Consumers looking to to travel to Mexico for vacation. Family or couples

Industry/Entity Type

Short term vacation rental industry

Coding

Coded - Design and coding required

Number of Pages Required

5+ page

Requirements
Must have
• Capabilities to accept credit card payments and link to other rental property sites calendars such as LODGR and Staynets
Nice to have
• Option for best plugins for property rental

```html
<!DOCTYPE html>
<html lang="en">
<head>
<meta charset="utf-8">
<title>Cedar Lantern Retreat — Bend, Oregon Vacation Home</title>
<link href="https://fonts.googleapis.com/css2?family=Gilda+Display&family=Inter:wght@300;400;500&display=swap" rel="stylesheet">
<style>
:root{
  --gold:#e7c25a;
  --gold-text:#c9a23e;
  --ink:#2b2b2b;
  --body:#4a4a4a;
  --dark:#323232;
  --card:#e6e6e6;
  --line:#dcdcdc;
  --white:#fff;
  --serif:"Gilda Display", Georgia, serif;
  --sans:"Inter", Helvetica, Arial, sans-serif;
}
*{box-sizing:border-box;margin:0;padding:0}
html,body{width:1200px;height:4073px;overflow:hidden}
body{position:relative;background:var(--white);font-family:var(--sans);color:var(--ink)}
.abs{position:absolute}
.kicker{font-family:var(--sans);font-size:11px;letter-spacing:2px;text-transform:uppercase;color:var(--gold-text)}
.serif{font-family:var(--serif);font-weight:400}
.btn{position:absolute;display:flex;align-items:center;justify-content:center;gap:8px;background:var(--gold);color:var(--ink);border-radius:22px;font-size:11px;letter-spacing:1.8px;text-transform:uppercase;font-weight:500;text-decoration:none}
.btn svg{width:12px;height:12px}
.center{left:0;width:100%;text-align:center}

/* nav */
.nav{top:0;left:0;width:1200px;height:49px;background:var(--white);border-bottom:1px solid #eee}
.logo{left:60px;top:12px;font-family:var(--serif);font-size:22px;letter-spacing:1.5px;color:var(--ink)}
.nav-links{left:400px;top:19px;display:flex;gap:39px;font-size:10.5px;letter-spacing:1.4px;color:#444}
.nav .btn{left:972px;top:10px;width:165px;height:30px;font-size:10px}

/* hero */
.hero{top:49px;left:0;width:1200px;height:574px;background:linear-gradient(180deg,#3a3633 0%,#4b4540 45%,#6a5f55 80%,#7a6a5a 100%)}
.hero-shade{inset:0;background:rgba(0,0,0,.35)}
.hero .kicker{top:76px;color:#eee;font-size:12px}
.hero h1{top:99px;font-size:54px;color:#fff}
.hero-sub{top:177px;left:270px;width:660px;text-align:center;font-size:13px;line-height:22px;color:#eee;font-weight:300}
.hero-facts{top:233px;display:flex;justify-content:center;gap:20px;font-size:13px;color:#f1f1f1}
.hero-facts span{display:flex;align-items:center;gap:7px}
.hero-facts i{width:8px;height:8px;border:1px solid #ccc;border-radius:50%;display:block}
.hero .btn{left:519px;top:280px;width:162px;height:42px}
.scroll-tab{left:570px;top:544px;width:60px;height:60px;border-radius:50%;background:#fff;display:flex;justify-content:center;align-items:flex-start;padding-top:24px}

/* house */
.frame{border:1px solid #e4cf9a}
.photo{background:linear-gradient(160deg,#8fb0c9 0%,#6e8a5a 45%,#4f6b3a 75%,#6a5a45 100%)}
.house-card{left:451px;top:757px;width:585px;height:367px;background:#fff;box-shadow:0 6px 24px rgba(0,0,0,.12)}
.house-card .kicker{left:49px;top:45px}
.house-card h2{left:49px;top:64px;font-size:38px}
.house-card p{left:49px;top:122px;width:470px;font-size:11.5px;line-height:18.7px;color:var(--body);font-weight:300}
.house-card .btn{left:49px;top:261px;width:216px;height:41px}
.leaf{background:radial-gradient(ellipse at center,rgba(0,0,0,.05),rgba(0,0,0,0) 70%)}

/* gallery */
.gallery-title{top:1255px;font-size:38px}
.tile{position:absolute;width:259px}
.tile .img{height:351px}
.tile h3{font-family:var(--serif);font-weight:400;font-size:20px;text-align:center;margin-top:10px}
.tile p{font-size:11.5px;text-align:center;color:var(--body);margin-top:6px;font-weight:300}
.tile .go{width:30px;height:30px;border-radius:50%;border:1px solid #777;margin:16px auto 0;display:flex;align-items:center;justify-content:center}
.tile .go.on{background:var(--gold);border-color:var(--gold)}
.img-bed{background:linear-gradient(135deg,#d9d6cf,#b8b2a6 60%,#8e8272)}
.img-kitchen{background:linear-gradient(135deg,#6a6a68,#4a4a48);position:relative}
.img-living{background:linear-gradient(135deg,#d6d3cc,#b4ada2 60%,#6e645a)}
.img-yard{background:linear-gradient(160deg,#7fa4c2,#3d5a34 45%,#8a7c6c 100%)}
.checkin{position:absolute;left:0;width:100%;text-align:center;color:#fff}
.checkin.label{top:108px;font-size:11px;letter-spacing:2px}
.checkin.brand{top:210px;display:flex;justify-content:center;align-items:center;gap:8px;font-family:var(--serif);font-size:22px}
.checkin.brand i{width:14px;height:14px;border-radius:50%;background:#fff;display:block}

/* explore */
.explore{top:1905px;left:0;width:1200px;height:633px;background:var(--dark);color:#fff}
.explore .kicker{left:90px;width:580px;text-align:center;top:125px}
.explore h2{left:90px;width:580px;text-align:center;top:143px;font-size:39px}
.places{left:200px;width:364px;text-align:center;font-family:var(--serif)}
.places div{position:absolute;left:0;width:100%}
.pl-1{top:229px;font-size:12px;color:#4d4d4d}
.pl-2{top:266px;font-size:13px;color:#8a8a8a}
.pl-3{top:296px;font-size:20px;color:#fff}
.pl-4{top:345px;font-size:13px;color:#8a8a8a}
.pl-5{top:381px;font-size:12px;color:#5a5a5a}
.pl-6{top:417px;font-size:12px;color:#444}
.explore .btn{left:291px;top:466px;width:180px;height:42px}
.aerial{left:707px;top:78px;width:430px;height:476px;background:linear-gradient(180deg,#6f9ccc 0%,#9bb5c8 12%,#4a5e48 30%,#7a7a6a 60%,#8c8578 100%)}

/* reviews */
.reviews .kicker{top:2612px}
.reviews h2{top:2638px;font-size:40px}
.review{position:absolute;top:2703px;width:328px;height:198px;background:var(--card);text-align:center;padding:0 16px}
.stars{margin-top:36px;color:var(--gold);font-size:15px;letter-spacing:2px}
.review p{margin-top:10px;font-size:11px;line-height:19.5px;color:#555;font-weight:300}
.author{margin-top:16px;display:flex;justify-content:center;align-items:center;gap:8px;font-family:var(--serif);font-size:12px}
.author i{width:30px;height:30px;border-radius:50%;background:#9b8d80;border:2px solid #fff;display:block}
.author em{font-style:normal;font-family:var(--sans);color:#999;font-size:10.5px}
.qmark{position:absolute;right:14px;top:14px;font-family:var(--serif);font-size:56px;color:#d2d2d2;line-height:1}
.arrow-btn{position:absolute;width:30px;height:30px;border-radius:50%;border:1px solid #888;display:flex;align-items:center;justify-content:center;background:#fff}

/* faq */
.photo-fire{background:linear-gradient(160deg,#6b5a4a,#4a3e33 40%,#8a7a6a 75%,#6e6558)}
.faq .kicker{left:528px;top:2995px}
.faq h2{left:528px;top:3017px;font-size:42px}
.faq-sub{left:528px;top:3072px;font-size:11.5px;color:#444}
.faq-list{left:528px;top:3105px;width:609px}
.q{position:relative;border-bottom:1px solid var(--line);font-family:var(--serif);font-size:17px;padding:8px 0 10px}
.q span{position:absolute;right:2px;top:6px;font-family:var(--sans);font-size:16px;color:#666;font-weight:300}
.q p{font-family:var(--sans);font-size:11px;line-height:19px;color:#555;margin-top:10px;width:470px;font-weight:300}
.faq .btn{left:528px;top:3405px;width:164px;height:42px}

/* cta */
.cta{left:60px;top:3523px;width:1077px;height:272px;background:var(--gold);text-align:center}
.cta .kicker{top:57px;color:#3a3a3a}
.cta h2{top:78px;font-size:40px}
.cta p{top:130px;font-size:11.5px;color:#444}
.cta .btn{left:400px;top:175px;width:277px;height:43px;background:transparent;border:1px solid #3a3a3a}

/* footer */
.footer{top:3795px;left:0;width:1200px;height:278px;background:var(--dark);color:#ddd}
.fcol{top:62px}
.fcol h4{font-family:var(--serif);font-weight:400;font-size:15px;color:#fff;margin-bottom:12px}
.fcol a{display:block;font-size:11px;line-height:20.5px;color:#d4d4d4;text-decoration:none}
.loc{display:flex;gap:12px;font-size:11px;line-height:20.5px}
.loc i{width:22px;height:22px;border-radius:50%;border:1px solid #ccc;display:flex;align-items:center;justify-content:center;flex:none}
.fcol a.btn{position:relative;display:flex;width:116px;height:28px;font-size:10px;line-height:1;margin-top:14px;color:var(--ink)}
.frule{left:60px;top:232px;width:1077px;height:1px;background:#4c4c4c}
.fbase{top:245px;font-size:10.5px;color:#bbb}
</style>
</head>
<body>

<header class="nav abs">
  <div class="logo abs">CEDAR LANTERN RETREAT</div>
  <nav class="nav-links abs"><span>HOME</span><span>THE HOUSE</span><span>GALLERY</span><span>EXPLORE BEND</span><span>REVIEWS</span><span>FAQ</span></nav>
  <a class="btn">Check Availability</a>
</header>

<section class="hero abs" role="img" aria-label="Living room with stone wall, wood stove and leather sofas">
  <div class="hero-shade abs"></div>
  <div class="kicker abs center">Cedar Lantern Retreat — Bend, Oregon</div>
  <h1 class="serif abs center">Your Home Away From Home in Bend.</h1>
  <p class="hero-sub abs">Relax, explore, and enjoy Bend from a welcoming vacation home just minutes from the Tanager Quarter, with comfortable spaces, a private backyard, and everything you need.</p>
  <div class="hero-facts abs center"><span><i></i>3 Bedrooms</span><span><i></i>2 Baths</span><span><i></i>Sleeps 6</span><span><i></i>Pet Friendly</span><span><i></i>Walk to Tanager</span></div>
  <a class="btn">Book Direct <svg viewBox="0 0 12 12"><path d="M1 6h9M7 3l3 3-3 3" fill="none" stroke="#2b2b2b" stroke-width="1.2"/></svg></a>
  <div class="scroll-tab abs"><svg width="12" height="8" viewBox="0 0 12 8"><path d="M2 2l4 4 4-4" fill="none" stroke="#333" stroke-width="1.3"/></svg></div>
</section>

<section class="house">
  <div class="leaf abs" style="left:1040px;top:670px;width:160px;height:160px" role="img" aria-label="Faint leaf sprig decoration"></div>
  <div class="frame abs" style="left:158px;top:696px;width:332px;height:453px"></div>
  <div class="photo abs" style="left:63px;top:711px;width:408px;height:438px" role="img" aria-label="Fenced backyard with lawn, tree and rock garden"></div>
  <div class="house-card abs">
    <div class="kicker abs">The House</div>
    <h2 class="serif abs">West Hollywood Curated</h2>
    <p class="abs">Settle into a thoughtfully equipped Bend home designed to make every part of your stay comfortable and relaxing. Enjoy inviting living spaces for gathering and unwinding, cozy bedrooms for a restful night, a well-equipped kitchen for preparing meals, and a private fenced backyard where you can enjoy the fresh Central Oregon air. With convenient amenities and plenty of space for up to six guests, Cedar Lantern Retreat offers the perfect place to relax between days spent exploring Bend.</p>
    <a class="btn">Check Availability <svg viewBox="0 0 12 12"><path d="M1 6h9M7 3l3 3-3 3" fill="none" stroke="#2b2b2b" stroke-width="1.2"/></svg></a>
  </div>
</section>

<section class="gallery">
  <div class="kicker abs center" style="top:1226px">Our Gallery</div>
  <h2 class="serif abs center gallery-title">Comfort Made for Your Stay.</h2>
  <div class="tile" style="left:63px;top:1361px">
    <div class="img img-bed" role="img" aria-label="Bedroom with queen bed and chandelier"></div>
    <h3>Bedrooms</h3><p>Cozy spaces designed for restful nights.</p>
    <div class="go"><svg width="12" height="12" viewBox="0 0 12 12"><path d="M1 6h9M7 3l3 3-3 3" fill="none" stroke="#333" stroke-width="1.1"/></svg></div>
  </div>
  <div class="tile" style="left:334px;top:1380px">
    <div class="img img-kitchen" role="img" aria-label="Kitchen and dining area">
      <div class="checkin label">CHECK IN</div>
      <div class="checkin brand"><i></i>Staynest</div>
    </div>
    <h3>Kitchen &amp; Dinning</h3><p>Cook, gather, and enjoy meals together.</p>
    <div class="go on"><svg width="12" height="12" viewBox="0 0 12 12"><path d="M1 6h9M7 3l3 3-3 3" fill="none" stroke="#333" stroke-width="1.1"/></svg></div>
  </div>
  <div class="tile" style="left:607px;top:1361px">
    <div class="img img-living" role="img" aria-label="Living room with TV console and ottoman"></div>
    <h3>Living Spaces</h3><p>Relax and unwind in comfort.</p>
    <div class="go"><svg width="12" height="12" viewBox="0 0 12 12"><path d="M1 6h9M7 3l3 3-3 3" fill="none" stroke="#333" stroke-width="1.1"/></svg></div>
  </div>
  <div class="tile" style="left:878px;top:1380px">
    <div class="img img-yard" role="img" aria-label="Backyard patio with outdoor seating under pines"></div>
    <h3>Backyard</h3><p>Enjoy private outdoor space.</p>
    <div class="go"><svg width="12" height="12" viewBox="0 0 12 12"><path d="M1 6h9M7 3l3 3-3 3" fill="none" stroke="#333" stroke-width="1.1"/></svg></div>
  </div>
</section>

<section class="explore abs">
  <div class="leaf abs" style="left:0;top:330px;width:160px;height:220px" role="img" aria-label="Faint leaf sprig decoration"></div>
  <div class="kicker abs">Explore Bend</div>
  <h2 class="serif abs">The Best of Bend, Right Nearby.</h2>
  <div class="places abs" style="top:0;height:440px">
    <div class="pl-1">Tanager Quarter</div>
    <div class="pl-2">Brightwater Lawn Pavilion</div>
    <div class="pl-3">Kettleback River</div>
    <div class="pl-4">Restaurants &amp; Breweries</div>
    <div class="pl-5">Downtown Bend</div>
    <div class="pl-6">Shopping</div>
  </div>
  <svg class="abs" style="left:190px;top:320px" width="520" height="14" viewBox="0 0 520 14"><path d="M4 3l4 4-4 4" fill="none" stroke="#c9a23e" stroke-width="1"/><line x1="18" y1="7" x2="501" y2="7" stroke="#c9a23e" stroke-width="1"/></svg>
  <svg class="abs" style="left:690px;top:100px" width="20" height="460" viewBox="0 0 20 460"><line x1="1" y1="0" x2="1" y2="454" stroke="#8a7a50"/><line x1="1" y1="0" x2="17" y2="0" stroke="#8a7a50"/><line x1="1" y1="454" x2="17" y2="454" stroke="#8a7a50"/></svg>
  <a class="btn">Explore Bend <svg viewBox="0 0 12 12"><path d="M1 6h9M7 3l3 3-3 3" fill="none" stroke="#2b2b2b" stroke-width="1.2"/></svg></a>
  <div class="aerial abs" role="img" aria-label="Aerial view of Bend neighborhoods along the river with mountains"></div>
</section>

<section class="reviews">
  <div class="leaf abs" style="left:1050px;top:2540px;width:150px;height:150px" role="img" aria-label="Faint leaf sprig decoration"></div>
  <div class="kicker abs center">Loved by Our Guests</div>
  <h2 class="serif abs center">Highly Rated by Our Guests</h2>
  <div class="arrow-btn" style="left:39px;top:2787px"><svg width="12" height="12" viewBox="0 0 12 12"><path d="M11 6H2M5 3L2 6l3 3" fill="none" stroke="#333" stroke-width="1.1"/></svg></div>
  <div class="review" style="left:88px"><div class="qmark">”</div><div class="stars">★★★★★</div><p>"Our group consisted of five adults and we were in Bend for a wedding. Maren's place suited our needs perfectly. The house is in a quiet neighborhood and only ..."</p><div class="author"><i></i>— Marcus <em>(Raleigh, North Carolina)</em></div></div>
  <div class="review" style="left:435px"><div class="qmark">”</div><div class="stars">★★★★★</div><p>"We loved our stay at Maren's house! The location was great and Bend is beautiful. The house is very comfortable, the decor is so cute and the backyard is peaceful..."</p><div class="author"><i></i>— Delia <em>(Los Alamitos, California)</em></div></div>
  <div class="review" style="left:783px"><div class="qmark">”</div><div class="stars">★★★★★</div><p>"Great house in Bend, charming and very clean. Quiet neighborhood—we enjoyed our stay here. Ample parking. Well equipped kitchen..."</p><div class="author"><i></i>— Rowan <em>(Salem, Oregon)</em></div></div>
  <div class="arrow-btn" style="left:1130px;top:2787px"><svg width="12" height="12" viewBox="0 0 12 12"><path d="M1 6h9M7 3l3 3-3 3" fill="none" stroke="#333" stroke-width="1.1"/></svg></div>
</section>

<section class="faq">
  <div class="frame abs" style="left:158px;top:2977px;width:332px;height:470px"></div>
  <div class="photo-fire abs" style="left:63px;top:2993px;width:408px;height:454px" role="img" aria-label="Patio with fire table and wicker chairs"></div>
  <div class="kicker abs">FAQ</div>
  <h2 class="serif abs">Everything You Need to Know</h2>
  <div class="faq-sub abs">Have a question about staying at Cedar Lantern Retreat? Find quick answers to the details that matter most.</div>
  <div class="faq-list abs">
    <div class="q">Is the home pet friendly?<span>+</span></div>
    <div class="q">Is parking available?<span>+</span></div>
    <div class="q">What are the check-in and check-out times?<span>×</span><p>Plan your arrival with ease using clear check-in and check-out information, helpful instructions, and everything you need for a smooth start and finish to your stay.</p></div>
    <div class="q">What is the cancellation policy?<span>+</span></div>
    <div class="q" style="border-bottom:none">How many guests can stay?<span>+</span></div>
  </div>
  <a class="btn">View All FAQ <svg viewBox="0 0 12 12"><path d="M1 6h9M7 3l3 3-3 3" fill="none" stroke="#2b2b2b" stroke-width="1.2"/></svg></a>
  <div class="leaf abs" style="left:1090px;top:3330px;width:110px;height:150px" role="img" aria-label="Faint leaf sprig decoration"></div>
</section>

<footer class="footer abs">
  <div class="fcol abs" style="left:63px"><h4>Explore</h4><a>Home</a><a>The House</a><a>Photo Gallery</a><a>Explore Bend</a><a>Guest Reviews</a><a>FAQ</a></div>
  <div class="fcol abs" style="left:266px"><h4>Your Stay</h4><a>Check Availability</a><a>Book Direct</a><a>Contact Us</a><a>House Rules</a></div>
  <div class="fcol abs" style="left:482px"><h4>Location</h4><div class="loc"><i><svg width="10" height="12" viewBox="0 0 10 12"><path d="M5 11S1 6.8 1 4.5a4 4 0 018 0C9 6.8 5 11 5 11z" fill="none" stroke="#ddd"/><circle cx="5" cy="4.5" r="1.3" fill="#ddd"/></svg></i><span>Bend, Oregon<br>Walk to the Tanager Quarter</span></div></div>
  <div class="fcol abs" style="left:745px"><h4>Check us On</h4><a>Staynest</a><a>Lodgr</a></div>
  <div class="fcol abs" style="left:928px"><h4>Book Direct</h4><a style="width:225px">Skip The Extra Steps And Reserve Your Stay Directly Through Cedar Lantern Retreat.</a><a class="btn">Book Direct</a></div>
  <div class="frule abs"></div>
  <div class="fbase abs" style="left:66px">© 2026 Cedar Lantern Retreat. All Rights Reserved.</div>
  <div class="fbase abs" style="right:63px">Privacy Policy · Terms &amp; Conditions · Cancellation Policy</div>
</footer>

<section class="cta abs">
  <div class="kicker abs center">Book Direct</div>
  <h2 class="serif abs center">Ready for Your Bend Getaway?</h2>
  <p class="abs center">Check your dates, find the perfect time to stay, and reserve Cedar Lantern Retreat directly.</p>
  <a class="btn">Get Instant Confirmation <svg viewBox="0 0 12 12"><path d="M1 6h9M7 3l3 3-3 3" fill="none" stroke="#2b2b2b" stroke-width="1.2"/></svg></a>
</section>

</body>
</html>
```